Business Card Design

Im a makeup artist looking for some business cards but need help with creating it.

Industry/Entity Type

Business

Contact Information for Business Card

Maren Holt
email maren.holt3@brivomail.com
phone number 0283640296

Requirements
Must have
• i have a logo that i think would work and that i have as my logo on Pixlora. i would like maybe something at the bottom on the card saying like me on Pixlora or something like that.
Nice to have
• Nice writing, my logo as the main item. So its what people are drawn too. to have a glossy card.

```html
<!DOCTYPE html>
<html lang="en">
<head>
<meta charset="utf-8">
<title>Makeup by Maren Holt – Business Card</title>
<link href="https://fonts.googleapis.com/css2?family=Pathway+Gothic+One&display=swap" rel="stylesheet">
<style>
  :root {
    --card-bg: #ffffff;
    --ink-dark: #1a1a1a;
    --ink-grey: #555555;
    --rule: #333333;
  }
  * { margin: 0; padding: 0; box-sizing: border-box; }
  html, body { width: 1200px; height: 741px; overflow: hidden; background: var(--card-bg); }
  .card {
    position: relative;
    width: 1200px;
    height: 741px;
    background: var(--card-bg);
    font-family: "Pathway Gothic One", sans-serif;
  }
  .brand {
    position: absolute;
    left: 168px;
    top: 168px;
    width: 864px;
    text-align: center;
    color: var(--ink-dark);
    letter-spacing: 0.06em;
    line-height: 1;
    text-transform: uppercase;
  }
  .brand__main { display: block; font-size: 120px; }
  .brand__sub { display: block; font-size: 58px; margin-top: 8px; }
  .person {
    position: absolute;
    left: 105px;
    top: 462px;
    color: var(--ink-grey);
  }
  .person__name {
    font-size: 52px;
    line-height: 1;
    padding: 0 0 4px 2px;
    width: 280px;
    border-bottom: 2px solid var(--rule);
    font-weight: 400;
  }
  .person__role { font-size: 34px; line-height: 1.1; margin-top: 2px; }
  .divider {
    position: absolute;
    left: 563px;
    top: 472px;
    width: 4px;
    height: 77px;
    background: var(--ink-dark);
  }
  .contact {
    position: absolute;
    left: 733px;
    top: 462px;
    color: var(--ink-grey);
    font-size: 29px;
    line-height: 42px;
    list-style: none;
  }
  .social {
    position: absolute;
    left: 0;
    width: 1160px;
    top: 614px;
    text-align: center;
    color: var(--ink-dark);
    font-size: 29px;
  }
</style>
</head>
<body>
  <main class="card">
    <div class="brand">
      <span class="brand__main">Makeup</span>
      <span class="brand__sub">by Maren Holt</span>
    </div>

    <div class="person">
      <h1 class="person__name">Maren Holt</h1>
      <p class="person__role">Projec manager</p>
    </div>

    <div class="divider"></div>

    <ul class="contact">
      <li>email: maren.holt3@brivomail.com</li>
      <li>Contact: 0283640296</li>
    </ul>

    <p class="social">Like me on Pixlora:htpp/.....</p>
  </main>
</body>
</html>
```